Builder of high-end, expensive tables and other furniture

Build a website that represents what we do. I want a luxury feel that appeals to those who can afford our products. We build very high end tables and other furniture using trees that have fallen or are standing dead. We never cut living trees. Trees are harvested, milled, and kiln dried. Then that lumber is meticulously turned into fine furniture using the best equipment. Our furniture prices range from $1,000-$20,000.

Trying to figure out how to raise my spend.

```html
<!DOCTYPE html>
<html lang="en">
<head>
<meta charset="utf-8">
<title>Heartwood Tables LLC</title>
<link href="https://fonts.googleapis.com/css2?family=Crimson+Text:wght@400;600&family=Montserrat:wght@400;500;600;700&display=swap" rel="stylesheet">
<style>
:root{
  --orange:#f07425;
  --blue:#0b4fa6;
  --black:#0d0d0d;
  --ink:#1d1d1d;
  --muted:#8a8a8a;
  --grey-panel:#ececec;
  --circle:#ededed;
  --line:#e2e2e2;
  --white:#ffffff;
}
*{margin:0;padding:0;box-sizing:border-box}
html,body{width:1200px;height:3692px;overflow:hidden;background:var(--white)}
body{position:relative;font-family:"Montserrat",sans-serif;color:var(--ink)}
.abs{position:absolute}
.photo{position:absolute}
.topbar{left:0;top:0;width:1200px;height:35px;background:var(--black);color:#fff;font-size:11px}
.topbar .info{position:absolute;top:11px;display:flex;align-items:center;gap:6px;white-space:nowrap}
.topbar .social{position:absolute;right:140px;top:10px;display:flex;gap:18px}
.topbar .social span{width:13px;height:13px;border:1.5px solid #fff;border-radius:50%}
.logo{font-family:"Crimson Text",serif;font-weight:600;display:flex;align-items:center;gap:6px;white-space:nowrap}
.logo .dot{width:12px;height:12px;border-radius:50%;background:var(--orange)}
.header-logo{left:141px;top:52px;font-size:28px;color:var(--blue)}
.nav{top:60px;left:485px;display:flex;gap:39px;font-size:12px;font-weight:500;white-space:nowrap}
.nav .active{color:var(--orange)}
.cart{left:994px;top:58px;display:flex;align-items:center;gap:6px;font-size:12px;font-weight:600}
.hero-title{left:141px;top:204px;width:350px;font-family:"Crimson Text",serif;font-weight:600;font-size:40px;line-height:46px;color:var(--black)}
.btn{position:absolute;background:var(--orange);color:#fff;font-size:12px;font-weight:600;display:flex;align-items:center;justify-content:center;letter-spacing:.3px;white-space:nowrap}
.arrows{position:absolute;display:flex;gap:9px}
.arrows span{width:39px;height:39px;display:flex;align-items:center;justify-content:center;border:1.5px solid var(--blue);color:var(--blue);font-size:16px}
.arrows span.next{background:var(--blue);color:#fff}
.cat{position:absolute;top:660px;width:140px;text-align:center;font-size:14px;font-weight:600;white-space:nowrap}
.cat .circ{width:103px;height:103px;border-radius:50%;margin:0 auto 18px;box-shadow:0 3px 6px rgba(0,0,0,.1)}
.dots{left:106px;top:1237px;width:80px;height:80px;background-image:radial-gradient(#cfcfcf 1.6px,transparent 1.8px);background-size:8px 8px}
.two-tone{font-weight:700}
.two-tone .o{color:var(--orange)}
.two-tone .b{color:var(--blue)}
.quality-title{left:607px;top:952px;font-size:31px;line-height:40px}
.quality-text{left:607px;top:1042px;width:400px;font-size:12px;line-height:21.5px;color:#333}
.quality-text p+p{margin-top:9px}
.section-title{position:absolute;left:0;width:1200px;text-align:center;font-size:31px}
.card{position:absolute;top:1438px;width:176px;height:225px;background:#fff;box-shadow:0 2px 12px rgba(0,0,0,.07);text-align:center}
.card .pic{position:absolute;left:22px;top:30px;width:132px;height:110px}
.card .heart{position:absolute;right:10px;top:16px;width:19px;height:19px;border-radius:50%;background:#d9d9d9}
.card h4{position:absolute;top:166px;left:0;width:100%;font-size:14px;font-weight:600;white-space:nowrap}
.card .add{position:absolute;top:191px;left:0;width:100%;font-size:11px;color:var(--muted)}
.card .add b{color:var(--orange);font-weight:400}
.collection{left:141px;top:1808px;width:919px;height:389px;background:var(--grey-panel)}
.collection .tab{position:absolute;left:53px;top:53px;width:87px;height:283px;background:#fff}
.collection h2{position:absolute;left:67px;top:64px;font-family:"Crimson Text",serif;font-weight:600;font-size:64px;line-height:68px}
.collection p{position:absolute;left:67px;top:212px;width:320px;font-size:12px;line-height:21.5px}
.feature{position:absolute;top:2280px;width:230px;text-align:center}
.feature .circ{width:86px;height:86px;border-radius:50%;background:var(--circle);margin:0 auto 14px;display:flex;align-items:center;justify-content:center}
.feature h4{font-size:16px;font-weight:600;margin-bottom:8px}
.feature p{font-size:12px;line-height:21px;color:#333}
.divider{left:141px;top:2528px;width:919px;height:1px;background:var(--line)}
.port{position:absolute;top:2677px;width:176px;height:227px}
.quote{left:233px;top:3058px;font-family:"Crimson Text",serif;font-size:170px;line-height:140px;color:#e6ebf2}
.review{left:290px;top:3098px;width:620px;text-align:center;font-size:12px;line-height:21.5px;color:#333}
.reviewer{left:0;top:3200px;width:1200px;text-align:center;font-size:13px;font-weight:600}
.footer{left:0;top:3360px;width:1200px;height:272px;background:var(--orange);color:#fff}
.footer .tree{position:absolute;left:0;top:0;width:230px;height:272px;background:radial-gradient(ellipse at 40% 60%,rgba(255,255,255,.12),transparent 70%)}
.footer-logo{position:absolute;left:141px;top:68px;font-size:28px;color:#fff}
.footer-logo .dot{background:#fff}
.footer .about{position:absolute;left:141px;top:112px;width:300px;font-size:12px;line-height:19px}
.footer .icons{position:absolute;left:141px;top:205px;display:flex;gap:9px}
.footer .icons span{width:24px;height:24px;border:1.5px solid #fff;border-radius:50%}
.footer h5{font-size:16px;font-weight:700;margin-bottom:16px;white-space:nowrap}
.footer ul{list-style:none;font-size:12px;line-height:23px;white-space:nowrap}
.col{position:absolute;top:74px}
.newsletter p{font-size:12px;line-height:19px;width:260px}
.signup{position:absolute;left:784px;top:3523px;width:276px;height:35px;background:#fff;border:2px solid #fff;display:flex;align-items:center;font-size:12px;color:#555}
.signup .field{flex:1;display:flex;align-items:center;gap:8px;padding-left:16px}
.signup .go{width:73px;height:100%;background:var(--blue);color:#fff;font-size:11px;font-weight:600;display:flex;align-items:center;justify-content:center}
.copyright{left:0;top:3632px;width:1200px;height:60px;background:var(--blue);color:#fff;font-size:12px;display:flex;align-items:center;justify-content:center}
</style>
</head>
<body>

<div class="topbar abs">
  <div class="info" style="left:141px">
    <svg width="10" height="13" viewBox="0 0 10 13"><path d="M5 0C2.2 0 0 2.2 0 5c0 3.5 5 8 5 8s5-4.5 5-8c0-2.8-2.2-5-5-5zm0 7a2 2 0 110-4 2 2 0 010 4z" fill="#fff"/></svg>
    48 Fallen Oak Road, Millbrook Valley
  </div>
  <div class="info" style="left:413px">
    <svg width="12" height="12" viewBox="0 0 12 12"><path d="M2.4 0.5l2 2.4-1.2 1.6c.8 1.7 2.2 3.1 3.9 3.9L8.7 7.2l2.4 2-1 2.3C5.4 11.4.6 6.6.5 1.5z" fill="#fff"/></svg>
    555-014-2290
  </div>
  <div class="social"><span></span><span></span><span></span><span></span></div>
</div>

<div class="logo header-logo abs"><span class="dot"></span>Heartwood Tables</div>
<nav class="nav abs">
  <span class="active">HOME</span><span>ABOUT US</span><span>SHOP</span><span>BLOG</span><span>CONTACT US</span>
  <svg width="14" height="14" viewBox="0 0 14 14" style="margin-left:-4px"><circle cx="6" cy="6" r="4.5" fill="none" stroke="#111" stroke-width="2"/><path d="M9.5 9.5L13 13" stroke="#111" stroke-width="2"/></svg>
</nav>
<div class="cart abs">
  <svg width="15" height="17" viewBox="0 0 15 17"><path d="M1.5 5h12v11h-12z M4.5 5V3.5a3 3 0 016 0V5" fill="none" stroke="#111" stroke-width="1.5"/></svg>
  $146.66
</div>

<div class="photo" role="img" aria-label="Modern dark wood kitchen with a marble island and a dining table with leather chairs" style="left:495px;top:100px;width:705px;height:495px;background:linear-gradient(180deg,#2e2b28 0%,#5a4f47 30%,#8a7a6b 55%,#b9aa98 70%,#cfcdc9 85%,#e4e3e0 100%)"></div>
<h1 class="hero-title abs">We Are Builder of High-end,Expensive Tables &amp; Other Furniture</h1>
<div class="btn" style="left:141px;top:404px;width:145px;height:42px">VIEW PRODUCTS</div>
<div class="arrows" style="left:141px;top:469px"><span>‹</span><span class="next">›</span></div>

<div class="cat" style="left:122px"><div class="circ" role="img" aria-label="Round glass designer table on a black base" style="background:radial-gradient(circle at 50% 50%,#3a3a3a 0%,#8c8c8c 30%,#ededed 55%)"></div>Designer Table</div>
<div class="cat" style="left:258px"><div class="circ" role="img" aria-label="Wooden dining table with upholstered chairs" style="background:radial-gradient(circle at 50% 50%,#b77b4c 0%,#d9c7b4 35%,#ededed 58%)"></div>Dining</div>
<div class="cat" style="left:393px"><div class="circ" role="img" aria-label="Upholstered bed with neutral bedding" style="background:radial-gradient(ellipse at 50% 55%,#8a7f73 0%,#c8beb1 35%,#ededed 60%)"></div>Bedrooms</div>
<div class="cat" style="left:529px"><div class="circ" role="img" aria-label="Amber lantern table lamp" style="background:radial-gradient(ellipse 22% 40% at 50% 50%,#e3a045 0%,#7a4a1e 60%,#ededed 100%)"></div>Lighting</div>
<div class="cat" style="left:665px"><div class="circ" role="img" aria-label="Gilded oval wall mirror" style="background:radial-gradient(ellipse 26% 40% at 50% 50%,#f3f1ec 0%,#f3f1ec 55%,#c09445 70%,#ededed 100%)"></div>Mirrors</div>
<div class="cat" style="left:800px"><div class="circ" role="img" aria-label="Dark iron garden lantern" style="background:radial-gradient(ellipse 22% 42% at 50% 50%,#4a3b4a 0%,#6b5a6a 55%,#ededed 100%)"></div>Garden</div>
<div class="cat" style="left:937px"><div class="circ" role="img" aria-label="Wooden outdoor lounge chair with cushion" style="background:radial-gradient(circle at 50% 50%,#a25b2f 0%,#d6a27a 32%,#ededed 58%)"></div>Outdoor Living</div>

<div class="dots abs"></div>
<div class="photo" role="img" aria-label="Warm living room with a cream sofa, dark coffee table and candles" style="left:156px;top:866px;width:389px;height:423px;background:linear-gradient(180deg,#d8cfa6 0%,#c7b88a 35%,#a69a78 55%,#3b342c 78%,#c8c3b6 100%)"></div>
<h2 class="two-tone quality-title abs"><span class="o">Quality Service &amp; High</span><br><span class="b">End Furnishings</span></h2>
<div class="quality-text abs">
  <p>Lorem ipsum dolor sitidunt&nbsp; amet consectetur adipiscing elitsed do eiusmod tempor incididunt labore dolore magna aliqua.</p>
  <p>Lorem ipsum dolor sit amet, consectetur adipiscing elit, sed do eiusmod tempor incididunt ut labore et dolore magna aliqua. Ut enim ad minim veniam, quis nostrud exercitation ullamco laboris nisi ut aliquip ex ea commodo consequat. Duis aute irure dolor in reprehenderit in voluptate velit esse cillum dolore eu fugiat.</p>
</div>

<h2 class="section-title two-tone" style="top:1370px"><span class="o">Our</span> <span class="b">Products</span></h2>
<div class="card" style="left:141px"><span class="heart"></span><div class="pic" role="img" aria-label="Walnut side table with drawers" style="background:radial-gradient(ellipse 50% 38% at 50% 50%,#9a552b 0%,#b06c3c 70%,#fff 100%)"></div><h4>Side Table</h4><div class="add">Add To Cart <b>→</b></div></div>
<div class="card" style="left:326px"><span class="heart"></span><div class="pic" role="img" aria-label="Dark bedside table with two drawers" style="background:radial-gradient(ellipse 38% 45% at 50% 50%,#2f2a27 0%,#3e3834 70%,#fff 100%)"></div><h4>Bedside Table</h4><div class="add">Add To Cart <b>→</b></div></div>
<div class="card" style="left:512px"><span class="heart"></span><div class="pic" role="img" aria-label="Upholstered bed" style="background:radial-gradient(ellipse 50% 35% at 50% 58%,#b5ab9e 0%,#d6cec3 70%,#fff 100%)"></div><h4>Bed</h4><div class="add">Add To Cart <b>→</b></div></div>
<div class="card" style="left:697px"><span class="heart"></span><div class="pic" role="img" aria-label="Round wooden pedestal table" style="background:radial-gradient(ellipse 42% 45% at 50% 50%,#b36f43 0%,#d99a6c 70%,#fff 100%)"></div><h4>Expensive Tables</h4><div class="add">Add To Cart <b>→</b></div></div>
<div class="card" style="left:883px"><span class="heart"></span><div class="pic" role="img" aria-label="Dining table with grey chairs" style="background:radial-gradient(ellipse 48% 42% at 50% 55%,#a06d48 0%,#c0c4c9 70%,#fff 100%)"></div><h4>Dining Table &amp; Chairs</h4><div class="add">Add To Cart <b>→</b></div></div>
<div class="arrows" style="left:557px;top:1686px"><span>‹</span><span class="next">›</span></div>

<section class="collection abs">
  <div class="tab"></div>
  <h2 class="two-tone"><span class="o">New</span><br><span class="b">Collection</span></h2>
  <p>Lorem ipsum dolor sit amet&nbsp; consec turiscing elised do eiusmod tempor incididunt ut labore.</p>
  <div class="btn" style="left:67px;top:274px;width:143px;height:39px">VIEW PRODUCTS</div>
  <div class="photo" role="img" aria-label="Living room with grey sofa, rattan pendant lamps and plants" style="left:439px;top:0;width:480px;height:389px;background:linear-gradient(180deg,#8d8c80 0%,#a3a295 40%,#7a7a76 62%,#b69362 80%,#c39a6a 100%)"></div>
</section>

<div class="feature" style="left:140px">
  <div class="circ"><svg width="44" height="44" viewBox="0 0 44 44" fill="none" stroke="#0b4fa6" stroke-width="1.8"><path d="M10 6h18l6 6v24H10z"/><path d="M15 14h10M15 19h12M15 24h6"/><circle cx="28" cy="28" r="6"/><path d="M32 32l6 6"/></svg></div>
  <h4>Wide Choice</h4><p>Lorem ipsum dolor sitamet<br>conseetur adip iscing...</p>
</div>
<div class="feature" style="left:370px">
  <div class="circ"><svg width="44" height="44" viewBox="0 0 44 44" fill="none" stroke="#0b4fa6" stroke-width="1.8"><path d="M12 6h20v32H12z"/><path d="M17 13h10M17 18h10M17 23h6"/><path d="M25 31l3 3 6-6"/></svg></div>
  <h4>Request A Quote</h4><p>Abore et dolore magna aliqua.<br>Ut enim ad minim...</p>
</div>
<div class="feature" style="left:599px">
  <div class="circ"><svg width="44" height="44" viewBox="0 0 44 44" fill="none" stroke="#0b4fa6" stroke-width="1.8"><circle cx="24" cy="24" r="12"/><path d="M24 17v7l5 3M20 8h8M24 8v4M4 20h6M2 26h8M6 32h6"/></svg></div>
  <h4>Recieve Fast Response</h4><p>Duis aute irure dolor prehenderit<br>in voluptate magna velit...</p>
</div>
<div class="feature" style="left:829px">
  <div class="circ"><svg width="44" height="44" viewBox="0 0 44 44" fill="none" stroke="#0b4fa6" stroke-width="1.8"><path d="M10 24v-4a12 12 0 0124 0v4"/><rect x="7" y="22" width="6" height="10" rx="2"/><rect x="31" y="22" width="6" height="10" rx="2"/><path d="M34 32c0 4-4 6-9 6"/><circle cx="22" cy="22" r="4"/></svg></div>
  <h4>24/7 Support</h4><p>Ut enim ad minim veniam quis<br>nostrud exercitation...</p>
</div>

<div class="divider abs"></div>

<h2 class="section-title two-tone" style="top:2610px"><span class="o">Our</span> <span class="b">Portfolio</span></h2>
<div class="port" style="left:141px;background:linear-gradient(180deg,#eae8e2 0%,#e2e0d9 55%,#9aa597 68%,#7f8a7c 78%,#d8d2c7 100%)" role="img" aria-label="Sage sofa under a pendant lamp"></div>
<div class="port" style="left:326px;background:linear-gradient(180deg,#e9e8e1 0%,#7e8d55 25%,#d7d6cf 50%,#6b4a30 75%,#3a2a1e 100%)" role="img" aria-label="Dining nook with hanging fern and wooden chairs"></div>
<div class="port" style="left:512px;background:linear-gradient(180deg,#d9c9b0 0%,#c4b397 45%,#8fb3b3 75%,#6e9ea2 100%)" role="img" aria-label="Lounge with teal chairs and a black floor lamp"></div>
<div class="port" style="left:697px;background:linear-gradient(180deg,#5e3422 0%,#7a4328 25%,#b8753f 55%,#8a4c27 100%)" role="img" aria-label="Wooden deck table with stools"></div>
<div class="port" style="left:883px;background:linear-gradient(180deg,#4f7a3a 0%,#6e8f4a 22%,#ece9de 42%,#3b4a3a 62%,#7a4a2c 80%,#8a5432 100%)" role="img" aria-label="Picnic tables in a gazebo"></div>
<div class="arrows" style="left:557px;top:2924px"><span>‹</span><span class="next">›</span></div>

<h2 class="section-title two-tone" style="top:3044px"><span class="o">Customer</span> <span class="b">Reviews</span></h2>
<div class="quote abs">“</div>
<p class="review abs">Lorem ipsum dolor sit amet, consectetuer adipiscing elit, sed diam nonummy nibh euismod tincidunt ut laoreet dolore magna aliquam erat volutpat. Ut wisi enim ad minim veniam, quis nostrud exerci tation ullamcorper suscipit lobortis nisl ut aliquip ex ea commodo consequat. Duis autem vel eum iriure dolor in hendrerit in vulputate velit.</p>
<div class="reviewer abs">- Marla Trent</div>
<div class="arrows" style="left:557px;top:3234px"><span>‹</span><span class="next">›</span></div>

<footer class="footer abs">
  <div class="tree"></div>
  <div class="logo footer-logo"><span class="dot"></span>Heartwood Tables</div>
  <p class="about">Lorem ipsum dolor sit amet consecter adipiscing elit, sed diam nonummy nibh euismod tincidunt ut laoreet dolore magna aliquam erat volutpat. Ut wisi enim ad minim veniam.</p>
  <div class="icons"><span></span><span></span><span></span><span></span></div>
  <div class="col" style="left:495px"><h5>Shop</h5><ul><li>All</li><li>Sale</li><li>Living</li><li>Bedroom</li><li>Kitchen</li></ul></div>
  <div class="col" style="left:611px"><h5>Links</h5><ul><li>About</li><li>Blog</li><li>Contact Us</li><li>FAQs</li><li>Terms &amp; Conditions</li></ul></div>
  <div class="col newsletter" style="left:782px"><h5>Join Our Newsletter</h5><p>Subscribe To Our Newsletter To Get The Latest Update To Your Inbox</p></div>
</footer>
<div class="signup">
  <div class="field"><svg width="14" height="10" viewBox="0 0 14 10" fill="none" stroke="#555"><rect x=".5" y=".5" width="13" height="9"/><path d="M.5.5L7 6l6.5-5.5"/></svg>Enter Email</div>
  <div class="go">SIGN UP</div>
</div>
<div class="copyright abs">© 2023 Heartwood Tables LLC. All Rights Reserved.</div>

</body>
</html>
```